Book Cover for: TITLE Mend the Quiet Hours SUBTITLE For couples who don't want to break up

We need a full cover design for a book on relationships written by husband and wife team, Marla and Walter Dunmore, PhD. This book will offer hope for couples that are on the verge of breaking up but want to work things out and stay together. The theme is to teach couples about their own reactions to their partner, how moods affect a relationship, how to get creative to solving problems and how to have a good feeling towards your partner regardless of differences. This book is about hope. It is a positive look at relationships that feel hopeless.

Target Market(s)

Married or couples that are going through a difficult time and are considering splitting up due to, communication difficulties, addiction, affair. We imagine the book will appeal to women more than men but still want a cover that men would be comfortable picking up.

Colors

Designer to choose colors to be used in the design.

Requirements
Must have
• We want the cover to beautiful, intriguing, simple and uncomplicated. We don't want it overly busy, technical, or complex.
Nice to have
• MAYBE?? a broken heart being put back together.
Should not have
• No photo, no cartoon, no flowers, no couple (unless obscure and not gender specific).

```html
<!DOCTYPE html>
<html lang="en">
<head>
<meta charset="utf-8">
<title>Mend the Quiet Hours — Book Cover</title>
<link rel="stylesheet" href="https://fonts.googleapis.com/css2?family=Barlow+Condensed:wght@600;700&family=Montserrat:wght@700&display=swap">
<style>
  :root {
    --page: #e4e4e4;
    --paper: #ffffff;
    --ink: #0a0a0a;
    --heart-red: #d10000;
  }
  html, body {
    margin: 0;
    padding: 0;
    width: 1200px;
    height: 1200px;
    overflow: hidden;
    background: var(--page);
  }
  .cover {
    position: absolute;
    left: 240px;
    top: 43px;
    width: 720px;
    height: 1114px;
    background: var(--paper);
    overflow: hidden;
  }
  .subtitle {
    position: absolute;
    top: 30px;
    left: 0;
    width: 100%;
    margin: 0;
    text-align: center;
    font-family: "Montserrat", sans-serif;
    font-weight: 700;
    font-size: 29px;
    line-height: 34px;
    letter-spacing: 0.5px;
    color: var(--ink);
    text-transform: uppercase;
  }
  .title {
    margin: 0;
    font-family: "Barlow Condensed", sans-serif;
    font-weight: 700;
    text-transform: uppercase;
  }
  .title-line {
    position: absolute;
    left: 0;
    width: 100%;
    text-align: center;
    display: block;
  }
  .title-top {
    top: 88px;
    font-size: 210px;
    line-height: 200px;
    color: var(--ink);
    letter-spacing: 2px;
  }
  .title-middle {
    top: 272px;
    height: 84px;
    display: flex;
    align-items: center;
    justify-content: center;
    gap: 14px;
    font-size: 96px;
    line-height: 84px;
    font-weight: 600;
    color: var(--ink);
  }
  .rule {
    width: 150px;
    height: 2px;
    background: var(--ink);
  }
  .title-bottom {
    top: 342px;
    font-size: 290px;
    line-height: 280px;
    color: var(--heart-red);
    letter-spacing: 2px;
  }
  .heart-art {
    position: absolute;
    left: 127px;
    top: 627px;
    width: 460px;
    height: 400px;
  }
  .authors {
    position: absolute;
    top: 1052px;
    left: 0;
    width: 100%;
    margin: 0;
    text-align: center;
    font-family: "Montserrat", sans-serif;
    font-weight: 700;
    font-size: 27px;
    letter-spacing: 0.5px;
    color: var(--ink);
    text-transform: uppercase;
  }
</style>
</head>
<body>
  <main class="cover">
    <p class="subtitle">For couples who<br>don't want to break up</p>
    <h1 class="title">
      <span class="title-line title-top">Mend</span>
      <span class="title-line title-middle"><span class="rule"></span>The Quiet<span class="rule"></span></span>
      <span class="title-line title-bottom">Hours</span>
    </h1>
    <svg class="heart-art" viewBox="0 0 460 400" role="img" aria-label="Red broken heart split down the middle, with two figures turned away from each other inside">
      <path d="M230 400 C120 320 0 220 0 110 C0 40 50 0 115 0 C170 0 210 35 230 65 C250 35 290 0 345 0 C410 0 460 40 460 110 C460 220 340 320 230 400 Z" fill="var(--heart-red)"/>
    </svg>
    <p class="authors">Marla &amp; Walter Dunmore, PhD.</p>
  </main>
</body>
</html>
```